Brightwell Auto Care 4x9 Rack Card

Design a 4" wide by 9" tall rack card printed front and back using the copy, logo and images uploaded below. I am also uploading a current flyer so you can see the typestyles we use. I will get the exact name of the font for you ASAP. Also will be uploading some before and after pictures for the back of the rack card

Target Market(s)

Affluent consumers who need their car cleaned and detailed in a meticulous fashion

Requirements
Must have
• Under the logo, put the words...... Premium Steam Detailing & Ceramic Coating.........also put ther following wording on the front side: Get Steamed! We use steam to clean your vehicle helping save millions of gallons of water and protecting our rivers, streams and lakes from runoff.
Nice to have
• a screened back background of hexagons might be nice

```html
<!DOCTYPE html>
<html lang="en">
<head>
<meta charset="utf-8">
<title>Brightwell Auto Care Rack Card</title>
<link rel="stylesheet" href="https://fonts.googleapis.com/css2?family=Quicksand:wght@400;500;700&family=Montserrat:wght@600;700&display=swap">
<style>
  :root {
    --stage: #6f6f6d;
    --paper: #ffffff;
    --blue: #3f7cc4;
    --green: #6aa84f;
    --ink: #2b2b2b;
    --rule: #8a8a8a;
    --hex-grey: #aeb0b0;
    --hero-light: #c9b48f;
    --hero-mid: #8c7455;
    --hero-blue: #3d5f9c;
    --hero-dark: #2e2a25;
  }
  * { box-sizing: border-box; margin: 0; padding: 0; }
  html, body { width: 1200px; height: 1200px; overflow: hidden; }
  body { background: var(--stage); font-family: "Quicksand", sans-serif; color: var(--ink); position: relative; }

  .card { position: absolute; top: 109px; width: 437px; height: 981px; background: var(--paper); overflow: hidden; border: 1px solid #3a3a3a; }
  .card--front { left: 126px; }
  .card--back { left: 637px; }

  .hero-photo {
    position: absolute; left: 0; top: 0; width: 434px; height: 446px;
    clip-path: polygon(0 0, 317px 0, 434px 205px, 296px 446px, 17px 446px, 0 425px);
    background: linear-gradient(125deg, var(--hero-light) 0%, var(--hero-mid) 38%, var(--hero-blue) 68%, var(--hero-dark) 100%);
  }

  .brand { position: absolute; display: flex; align-items: center; gap: 10px; }
  .brand__dot { border-radius: 50%; background: var(--green); flex: none; }
  .brand__name { font-family: "Quicksand", sans-serif; font-weight: 700; color: var(--green); white-space: nowrap; }
  .card--front .brand { left: 0; right: 0; top: 500px; justify-content: center; }
  .card--front .brand__dot { width: 38px; height: 38px; }
  .card--front .brand__name { font-size: 29px; }
  .card--back .brand { left: 20px; top: 26px; gap: 8px; }
  .card--back .brand__dot { width: 24px; height: 24px; }
  .card--back .brand__name { font-size: 16px; }

  .headline { position: absolute; left: 0; right: 0; top: 580px; text-align: center; color: var(--blue); font-weight: 400; font-size: 27px; line-height: 35px; letter-spacing: .2px; }
  .intro { position: absolute; left: 30px; right: 30px; top: 693px; text-align: center; font-size: 11.5px; line-height: 15px; }

  .contact { position: absolute; left: 43px; top: 783px; width: 220px; }
  .contact__title { font-family: "Montserrat", sans-serif; font-weight: 700; font-size: 13.5px; line-height: 18.5px; color: var(--ink); }
  .bullets { list-style: none; }
  .bullets li { position: relative; padding-left: 11px; font-size: 11.5px; line-height: 15px; }
  .bullets li::before { content: ""; position: absolute; left: 0; top: 5px; width: 4px; height: 4px; border-radius: 50%; background: var(--green); }
  .contact .bullets { margin-top: 12px; }
  .locations { position: absolute; left: 268px; top: 783px; height: 124px; border-left: 1px solid var(--rule); padding-left: 12px; width: 160px; }
  .locations .bullets li { margin-bottom: 9px; }

  .tagline { position: absolute; left: 0; right: 0; top: 938px; text-align: center; font-weight: 700; font-size: 21px; }
  .card--front .tagline { color: var(--blue); }
  .card--back .tagline { color: var(--green); }

  .hex { position: absolute; width: 210px; height: 181px; clip-path: polygon(25% 0, 75% 0, 100% 50%, 75% 100%, 25% 100%, 0 50%); }
  .hex--interior { background: linear-gradient(160deg, #6d6d6d, #2e2e2e); }
  .hex--engine { background: linear-gradient(160deg, #7a7a78, #3a3b3b); }
  .hex--shifter { background: linear-gradient(160deg, #575757, #202020); }
  .hex--grey { background: var(--hex-grey); }

  .before-after { position: absolute; left: 230px; width: 142px; top: 600px; text-align: center; color: var(--green); font-size: 27px; line-height: 28px; }

  .price { position: absolute; text-align: center; font-size: 11.5px; line-height: 14.5px; text-transform: uppercase; }
  .price strong { font-family: "Montserrat", sans-serif; font-weight: 700; font-size: 11px; }
  .price-rule { position: absolute; width: 1px; background: var(--rule); }
  .quote-note { position: absolute; left: 0; right: 0; top: 900px; text-align: center; font-size: 11.5px; }
</style>
</head>
<body>
  <section class="card card--front">
    <div class="hero-photo" role="img" aria-label="Detailer in blue shirt steam-cleaning the front grille of a luxury car in a garage"></div>

    <div class="brand"><span class="brand__dot"></span><span class="brand__name">Brightwell Auto Care</span></div>

    <h1 class="headline">PREMIUM STEAM<br>DETAILING &amp;<br>CERAMIC COATING</h1>

    <p class="intro">Get Steamed!<br>We use steam to clean your vehicle helping<br>save millions of gallons of water and protecting our rivers,<br>streams and lakes from runoff.</p>

    <div class="contact">
      <h2 class="contact__title">CALL FOR<br>INFORMATION &amp;<br>SCHEDULING:</h2>
      <ul class="bullets">
        <li>Boulder&nbsp; (720) 555-0142</li>
        <li>Vail&nbsp; (970) 555-0187</li>
        <li>Aspen/Snowmass (970) 555-0163</li>
      </ul>
    </div>

    <div class="locations">
      <ul class="bullets">
        <li>1420 Larkspur Avenue @ The Canyon Commons Boulder</li>
        <li>52 Aspenleaf Lane Snowmass Village</li>
        <li>318 Ridgeline Rd #104 Avon</li>
      </ul>
    </div>

    <p class="tagline">Fall In Love With Your Car Again!</p>
  </section>

  <section class="card card--back">
    <div class="brand"><span class="brand__dot"></span><span class="brand__name">Brightwell Auto Care</span></div>

    <div class="hex hex--grey" style="left:370px;top:-94px"></div>
    <div class="hex hex--grey" style="left:370px;top:110px"></div>
    <div class="hex hex--grey" style="left:370px;top:307px"></div>
    <div class="hex hex--grey" style="left:370px;top:504px"></div>

    <div class="hex hex--interior" style="left:201px;top:12px" role="img" aria-label="Before: dirty car interior floor and seat"></div>
    <div class="hex hex--interior" style="left:29px;top:110px" role="img" aria-label="After: clean car interior floor and seat"></div>
    <div class="hex hex--engine" style="left:201px;top:209px" role="img" aria-label="Before: dusty engine bay"></div>
    <div class="hex hex--engine" style="left:29px;top:307px" role="img" aria-label="After: steam-cleaned engine bay"></div>
    <div class="hex hex--shifter" style="left:201px;top:406px" role="img" aria-label="Before: dirty gear shifter console"></div>
    <div class="hex hex--shifter" style="left:29px;top:504px" role="img" aria-label="After: clean gear shifter console"></div>

    <p class="before-after">BEFORE<br>AND<br>AFTER</p>

    <p class="price" style="left:22px;width:140px;top:714px">Premium<br>Steam Washes<br>Starting at<br><strong>$100 AND UP</strong></p>
    <span class="price-rule" style="left:154px;top:712px;height:62px"></span>
    <p class="price" style="left:152px;width:140px;top:714px">Full<br>Steam Detailing<br>Starting at<br><strong>$275 AND UP</strong></p>
    <span class="price-rule" style="left:288px;top:712px;height:62px"></span>
    <p class="price" style="left:286px;width:130px;top:714px">Headlight<br>Restoration<br><strong>$110</strong></p>

    <p class="price" style="left:78px;width:160px;top:803px">Paint Correction<br>(Multi-Stage Polishing)<br>Starting at<br><strong>$650 AND UP</strong></p>
    <span class="price-rule" style="left:247px;top:800px;height:63px"></span>
    <p class="price" style="left:248px;width:120px;top:803px">Engine Steam<br>Cleaning<br><strong>- $75</strong></p>

    <p class="quote-note">Ceramic Coating - Call or visit us for a Quote</p>

    <p class="tagline">Fall In Love With Your Car Again!</p>
  </section>
</body>
</html>
```